Flyer Design Project

We need a flyer design for our company based in Ontario, Canada called CrateNest. We rent out plastic reusable moving boxes. Please visit Cratenest.ca to find out more information about our company. We are looking for a creative, clean, and fun flyer design. The flyers purpose is to share with others what services CrateNest offers as well as how convient our service is while still being cheaper than cardboard boxes.

Industry/Entity Type

Plastic

```html
<!DOCTYPE html>
<html lang="en">
<head>
<meta charset="utf-8">
<title>CrateNest Flyer</title>
<link rel="stylesheet" href="https://fonts.googleapis.com/css2?family=Arimo:wght@400;700&display=swap">
<style>
  :root {
    --green: #3fb23b;
    --green-soft: #7cbf2e;
    --black: #121212;
    --charcoal: #3a3a3a;
    --grey-text: #8c8c8c;
    --white: #ffffff;
    --page-bg: #ececec;
    --curl-light: #f2f2f2;
    --curl-dark: #9a9a9a;
  }
  * { box-sizing: border-box; margin: 0; padding: 0; }
  html, body {
    width: 1200px; height: 1000px; overflow: hidden;
    background: var(--page-bg);
    font-family: "Arimo", Arial, sans-serif;
  }
  .flyer {
    position: absolute; left: 60px; top: 150px;
    width: 1080px; height: 700px; overflow: hidden;
    box-shadow: 0 6px 18px rgba(0,0,0,.25);
  }
  .flyer-shapes { position: absolute; inset: 0; }
  .phone-line {
    position: absolute; left: 50px; top: 40px;
    display: flex; align-items: center; gap: 26px;
    color: var(--white); font-weight: 700; font-size: 42px; letter-spacing: .5px;
  }
  .tagline-box {
    position: absolute; left: 50px; top: 108px; width: 450px; height: 104px;
    background: #0b0b0b; border-radius: 8px;
    display: flex; align-items: center; justify-content: center; text-align: center;
    color: var(--grey-text); font-weight: 700; font-size: 31px; line-height: 1.15;
  }
  .price-badge {
    position: absolute; left: 700px; top: 20px; width: 170px; height: 130px;
    border-radius: 50%; background: var(--green-soft);
    border: 5px solid #d8d8d8;
    display: flex; flex-direction: column; align-items: center; justify-content: center;
    color: var(--white); font-weight: 700; transform: rotate(-8deg);
  }
  .price-badge .price { font-size: 40px; line-height: 1; }
  .price-badge .package { font-size: 16px; margin-top: 4px; }
  .step-art { position: absolute; background: var(--green-soft); }
  .step-art.truck { left: 340px; top: 250px; width: 210px; height: 130px; border-radius: 14px 40px 14px 14px; }
  .step-art.crate { left: 600px; top: 250px; width: 140px; height: 120px; border-radius: 10px; transform: rotate(-15deg); }
  .step-art.home { left: 830px; top: 170px; width: 130px; height: 100px; border-radius: 8px; }
  .step-note {
    position: absolute; color: var(--white); font-weight: 700; font-size: 13px; line-height: 1.2;
  }
  .step-note.truck-note { left: 355px; top: 262px; width: 120px; }
  .step-note.crate-note { left: 600px; top: 170px; width: 170px; transform: rotate(-25deg); text-align: center; }
  .step-note.home-note { left: 830px; top: 285px; width: 130px; text-align: center; }
  .why {
    position: absolute; left: 410px; top: 440px; color: var(--white);
  }
  .why .why-lead { font-weight: 700; font-size: 44px; }
  .why .why-name { font-weight: 700; font-size: 46px; color: var(--grey-text); margin-top: 4px; }
  .why .why-sub { font-size: 18px; margin-top: 6px; }
  .reasons {
    position: absolute; left: 160px; top: 350px; list-style: none;
  }
  .reasons li {
    display: flex; align-items: center; gap: 12px; height: 62px;
    color: var(--white);
  }
  .reasons .num { font-weight: 700; font-size: 52px; width: 34px; }
  .reasons .label { font-size: 22px; line-height: 1.1; }
  .brand-panel {
    position: absolute; left: 868px; top: 470px; width: 212px; height: 230px;
    background: var(--white);
    display: flex; flex-direction: column; align-items: center; justify-content: center; gap: 22px;
  }
  .brand-name {
    display: flex; align-items: center; gap: 10px;
    font-weight: 700; font-size: 28px; color: var(--black);
  }
  .brand-name .brand-square { width: 22px; height: 22px; background: var(--black); }
  .brand-site { font-size: 19px; font-weight: 700; color: #666; }
</style>
</head>
<body>
<main class="flyer">
  <svg class="flyer-shapes" width="1080" height="700" viewBox="0 0 1080 700" aria-hidden="true">
    <defs>
      <linearGradient id="dark-field" x1="0" y1="0" x2="0" y2="1">
        <stop offset="0" stop-color="#3a3a3a"/>
        <stop offset="1" stop-color="#0e0e0e"/>
      </linearGradient>
      <linearGradient id="curl" x1="0" y1="0" x2="1" y2="1">
        <stop offset="0" stop-color="#f2f2f2"/>
        <stop offset="1" stop-color="#9a9a9a"/>
      </linearGradient>
    </defs>
    <rect width="1080" height="700" fill="url(#dark-field)"/>
    <path class="green-sweep" fill="#3fb23b" stroke="#ffffff" stroke-width="5"
      d="M300,230 L450,350 H405 V530 C405,600 450,640 520,640 H950 C1040,640 1080,590 1080,470 V705 H-5 V620 C90,600 150,560 150,500 V360 H100 Z"/>
    <path class="corner-green" fill="#3fb23b" d="M600,0 H1080 V320 C1040,200 960,60 600,0 Z"/>
    <path class="page-curl" fill="url(#curl)" d="M600,0 C760,20 880,40 930,120 C900,60 820,30 600,0 Z M600,0 C800,30 920,60 980,140 C940,50 820,15 600,0 Z"/>
  </svg>

  <div class="phone-line">
    <svg width="50" height="50" viewBox="0 0 50 50" aria-hidden="true">
      <path fill="#7cbf2e" d="M14 6 l8 10 -5 5 c3 6 7 10 13 13 l5 -5 10 8 -4 7 c-16 2 -32 -14 -30 -30 z"/>
      <path fill="none" stroke="#7cbf2e" stroke-width="3" d="M28 8 a14 14 0 0 1 14 14 M28 15 a7 7 0 0 1 7 7"/>
    </svg>
    <span class="phone-number">1-800-555-0142</span>
  </div>

  <div class="tagline-box">Plastic, stackable,<br>eco-friendly moving boxes</div>

  <div class="price-badge">
    <span class="price">$ 99</span>
    <span class="package">Basic Package</span>
  </div>

  <div class="step-art truck" role="img" aria-label="Green delivery truck illustration"></div>
  <p class="step-note truck-note">We deliver your moving boxes right to your Main door</p>

  <div class="step-art crate" role="img" aria-label="Green open moving box with tape illustration"></div>
  <p class="step-note crate-note">Pack it up! Our boxes protect your belongings and make stacking safe.</p>

  <div class="step-art home" role="img" aria-label="Green house illustration"></div>
  <p class="step-note home-note">Once you're unpacked we'll come by your new home and collect the moving boxes.</p>

  <div class="why">
    <p class="why-lead">Why choose</p>
    <p class="why-name">CRATENEST?</p>
    <p class="why-sub">We have 5 good reasons</p>
  </div>

  <ol class="reasons">
    <li><span class="num">1</span><span class="label">We<br>deliver</span></li>
    <li><span class="num">2</span><span class="label">Pack<br>securely</span></li>
    <li><span class="num">3</span><span class="label">Safely<br>stack</span></li>
    <li><span class="num">4</span><span class="label">We<br>pickup</span></li>
    <li><span class="num">5</span><span class="label">Environmentally<br>friendly</span></li>
  </ol>

  <div class="brand-panel">
    <p class="brand-name"><span class="brand-square"></span>CRATENEST</p>
    <p class="brand-site">www.cratenest.ca</p>
  </div>
</main>
</body>
</html>
```